Blue Heron IT Business Card - Clean, Simple

Need a simple, clean standard sized business card for an IT consulting business using existing logo and company colours. Background should be mainly white. Feel free to be creative but clean, simple, quiet design is preferred. Font is specified in logo but any sans serif fonts work.

Contact Information for card is as follows (doesn't need to be in this exact order):

Martin Calloway
Owner
martin@blueheronit.ca
705-391-2586
www.blueheronit.ca

Target Market(s)

Small to medium sized business.

Industry/Entity Type

IT Consulting

Contact Information for Business Card

Logo and contact info.

Font styles to use
Sans Serif

Colors
EE7325
F08F49
F5BC92
FAE3D3
FDF4ED

Requirements
Must have
• All white or mostly white background.

```html
<!DOCTYPE html>
<html lang="en">
<head>
<meta charset="utf-8">
<title>Blue Heron IT – Business Card</title>
<link rel="stylesheet" href="https://fonts.googleapis.com/css2?family=Open+Sans:wght@400;600;700&display=swap">
<style>
  :root {
    --stage: #313131;
    --brand-orange: #EE7325;
    --brand-orange-light: #F08F49;
    --card-white: #FFFFFF;
    --ink: #2B2B2B;
    --rule: #111111;
  }
  * { box-sizing: border-box; margin: 0; padding: 0; }
  html, body {
    width: 1200px;
    height: 780px;
    overflow: hidden;
    background: var(--stage);
    font-family: "Open Sans", Arial, sans-serif;
  }
  .sheet {
    position: relative;
    width: 1200px;
    height: 780px;
    display: flex;
    align-items: center;
    justify-content: center;
    gap: 40px;
  }
  .card {
    position: relative;
    width: 540px;
    height: 309px;
    overflow: hidden;
  }

  /* Back of card */
  .card--back {
    background: var(--brand-orange);
    display: flex;
    align-items: center;
    justify-content: center;
  }
  .brand-name {
    color: var(--card-white);
    font-weight: 700;
    font-size: 40px;
    letter-spacing: 0.5px;
  }

  /* Front of card */
  .card--front {
    background: var(--card-white);
    border-bottom: 4px solid var(--brand-orange);
  }
  .identity {
    position: absolute;
    right: 232px;
    top: 118px;
    text-align: right;
  }
  .person-name {
    font-size: 26px;
    font-weight: 700;
    line-height: 1.1;
    white-space: nowrap;
  }
  .person-name .first { color: var(--brand-orange); }
  .person-name .last { color: var(--ink); }
  .person-role {
    font-size: 15px;
    font-weight: 400;
    color: var(--ink);
    letter-spacing: 0.5px;
    margin-top: 2px;
  }
  .divider {
    position: absolute;
    left: 322px;
    top: 96px;
    width: 2px;
    height: 112px;
    background: var(--rule);
  }
  .contact-list {
    position: absolute;
    left: 338px;
    top: 106px;
    list-style: none;
  }
  .contact-item {
    display: flex;
    align-items: center;
    gap: 8px;
    font-size: 14px;
    color: var(--ink);
    line-height: 1;
    margin-bottom: 12px;
    white-space: nowrap;
  }
  .contact-icon {
    width: 16px;
    height: 16px;
    flex: none;
  }
</style>
</head>
<body>
<main class="sheet">

  <section class="card card--back" aria-label="Card back">
    <div class="brand-name">Blue Heron IT</div>
  </section>

  <section class="card card--front" aria-label="Card front">
    <div class="identity">
      <div class="person-name"><span class="first">Martin</span> <span class="last">Calloway</span></div>
      <div class="person-role">Owner</div>
    </div>

    <div class="divider"></div>

    <ul class="contact-list">
      <li class="contact-item">
        <svg class="contact-icon" viewBox="0 0 16 16" aria-hidden="true">
          <path fill="var(--brand-orange)" d="M3.6 1.5l2.2 2.6-1.3 1.6c.8 1.8 2.2 3.2 4 4l1.6-1.3 2.6 2.2-1.2 2.3C7 12.6 3.4 9 2.1 4.2z"/>
        </svg>
        <span>705-391-2586</span>
      </li>
      <li class="contact-item">
        <svg class="contact-icon" viewBox="0 0 16 16" aria-hidden="true">
          <circle cx="8" cy="8" r="6.5" fill="none" stroke="var(--brand-orange)" stroke-width="1.6"/>
          <ellipse cx="8" cy="8" rx="2.8" ry="6.5" fill="none" stroke="var(--brand-orange)" stroke-width="1.2"/>
          <line x1="1.5" y1="8" x2="14.5" y2="8" stroke="var(--brand-orange)" stroke-width="1.2"/>
        </svg>
        <span>www.blueheronit.ca</span>
      </li>
      <li class="contact-item">
        <svg class="contact-icon" viewBox="0 0 16 16" aria-hidden="true">
          <rect x="1.5" y="3.5" width="13" height="9" rx="1" fill="none" stroke="var(--brand-orange)" stroke-width="1.5"/>
          <path d="M2 4l6 5 6-5" fill="none" stroke="var(--brand-orange)" stroke-width="1.5"/>
        </svg>
        <span>martin@blueheronit.ca</span>
      </li>
    </ul>
  </section>

</main>
</body>
</html>
```